Design profile for MuroDeck Nordhaven

I had a logo competition here recently, and was left with two logos that I could not choose between. Therefore, I create this competition where I want a complete design package or a visual identity for the company. I want you to create design elements that can be used both in print and online. (letterhead, envelopes, business card, website, facebook, etc.) I have also attached a picture of the car I have ordered. I'm happy if you can show how the design can be used on that as well.
What is important is that the logos are treated individually, and that the design you create reflects or builds up under the logo. I want the design to be recognizable and to have a connection with the logo and what we do. (take fizzo lumo as an example. if you remove the name, but keep the red color and the white line, then you will recognize which brand it is about right away)
You choose whether you want to make proposals only for one logo, or or both, but it is important that they are treated individually. The best overall package determines which logo I use.
I have also added an image that you can use as an example background if you want it in a facebook banner for example.
It is important that the design looks professional and unique. A number of designs have come in, but many of the designs are very similar and general. Here is a video of the printer if you need inspiration: https://clipvault.example/v/Q8ZtrMx2LwK

Industry/Entity Type

WallPrinting

Requirements
Must have
• Unique an professional design that can be used both online and print
Nice to have
• Show how to use the design on a VX Tully. (see photos attached)
Should not have
• The design can be simple, but not too simple and general. I want it to give the company an identity

```html
<!DOCTYPE html>
<html lang="en">
<head>
<meta charset="utf-8">
<title>MuroDeck Nordhaven – Stationery Set</title>
<link href="https://fonts.googleapis.com/css2?family=Montserrat:wght@400;500;600;700&family=Arimo:wght@400;700&family=Great+Vibes&display=swap" rel="stylesheet">
<style>
  :root{
    --blue:#0b9bd8;
    --blue-deep:#0686c0;
    --orange:#f26b21;
    --yellow:#f5c400;
    --red:#d0202e;
    --ink:#1d2733;
    --grey:#6b7480;
    --paper:#ffffff;
    --stage:#e7e8ea;
    --line:#c9ced4;
  }
  *{box-sizing:border-box;margin:0;padding:0}
  html,body{width:1200px;height:4397px;overflow:hidden}
  body{background:var(--stage);font-family:"Arimo",Arial,sans-serif;color:var(--ink);position:relative}
  .piece{position:absolute;overflow:hidden;box-shadow:0 10px 28px rgba(0,0,0,.18)}
  .piece svg.wave{position:absolute;left:0;bottom:0;width:100%}
  .white{background:var(--paper)}
  .blue{background:var(--blue)}

  /* brand name block */
  .brand{display:flex;align-items:center;gap:12px;font-family:"Montserrat",sans-serif;font-weight:600;letter-spacing:.5px;line-height:1.05}
  .brand .mark{width:22px;height:22px;background:currentColor;flex:none}
  .brand.dark{color:var(--ink)}
  .brand.light{color:#fff}

  /* business cards */
  .card{width:500px;height:286px;top:110px}
  .card-front{left:60px}
  .card-back{left:640px;border-bottom:5px solid var(--yellow)}
  .card-front .brand{position:absolute;left:34px;top:96px;font-size:26px}
  .card-front .divider{position:absolute;left:262px;top:40px;width:2px;height:128px;background:var(--blue)}
  .card-front .contact{position:absolute;left:282px;top:38px;font-size:12px;line-height:1.55}
  .person{font-family:"Montserrat",sans-serif;font-weight:700;font-size:15px;letter-spacing:.3px}
  .person .first{color:var(--blue)}
  .person .last{color:var(--red)}
  .role{color:var(--ink);margin-bottom:6px}
  .ico{display:inline-block;width:11px;height:11px;vertical-align:-1px;margin-right:5px}
  .card-back .brand{position:absolute;left:0;right:0;top:110px;justify-content:center;font-size:36px}

  /* letterhead */
  .letterhead{left:300px;top:520px;width:600px;height:849px}
  .lh-head{position:absolute;left:50px;right:50px;top:50px;height:70px}
  .lh-head .brand{position:absolute;left:0;top:18px;font-size:24px}
  .lh-head .addr{position:absolute;right:0;top:8px;font-size:10px;line-height:1.6;text-align:right;color:var(--ink)}
  .lh-rule{position:absolute;left:50px;right:50px;top:130px;height:2px;background:var(--blue)}
  .letter{position:absolute;left:50px;right:70px;top:160px;font-size:11px;line-height:1.65;color:#333}
  .letter p{margin-bottom:12px}
  .letter .sign{font-family:"Great Vibes",cursive;font-size:26px;color:var(--ink);margin-top:4px}

  /* envelopes */
  .env{top:1460px;width:520px;height:260px}
  .env-front{left:40px}
  .env-back{left:640px}
  .env-front .brand{position:absolute;left:28px;top:26px;font-size:18px}
  .env-front .addr{position:absolute;left:28px;top:62px;font-size:11px;line-height:1.5}
  .env-back .brand{position:absolute;left:0;right:0;top:104px;justify-content:center;font-size:32px}

  /* folder */
  .folder{position:absolute;left:180px;width:840px;height:540px;display:flex;box-shadow:0 10px 28px rgba(0,0,0,.18)}
  .folder-out{top:1820px}
  .folder-in{top:2440px}
  .panel{position:relative;width:420px;height:540px;overflow:hidden}
  .panel + .panel{border-left:1px solid #d6dade}
  .panel svg.wave{position:absolute;left:0;bottom:0;width:100%}
  .fold-back .brand{position:absolute;left:0;right:0;top:120px;justify-content:center;font-size:30px}
  .fold-back .foot{position:absolute;left:24px;right:24px;bottom:22px;font-size:10px;color:#fff;display:flex;gap:14px;flex-wrap:wrap}
  .fold-front .brand{position:absolute;left:0;right:0;top:64px;justify-content:center;font-size:26px}
  .pocket{position:absolute;left:0;right:0;bottom:0;height:150px;background:var(--blue)}
  .pocket.left{clip-path:polygon(0 0,70% 0,100% 100%,0 100%)}
  .pocket.right{clip-path:polygon(0 20%,100% 0,100% 100%,0 100%)}
  .insert{position:absolute;left:40px;top:34px;width:330px;height:420px;background:#fff;box-shadow:0 2px 8px rgba(0,0,0,.15);padding:20px 22px;font-size:8px;line-height:1.6;color:#444}
  .insert .brand{font-size:14px;gap:7px}
  .insert .brand .mark{width:12px;height:12px}
  .insert .rule{height:1.5px;background:var(--blue);margin:10px 0 14px}

  /* cover & notepad */
  .cover{left:150px;top:3120px;width:420px;height:600px}
  .cover .brand{position:absolute;left:0;right:0;top:260px;justify-content:center;font-size:34px}
  .notepad{left:630px;top:3120px;width:420px;height:600px}
  .notepad .brand{position:absolute;left:0;right:0;top:36px;justify-content:center;font-size:20px}
  .notepad .date{position:absolute;right:30px;top:86px;font-size:11px;color:var(--grey)}
  .notepad .lines{position:absolute;left:30px;right:30px;top:118px}
  .notepad .lines span{display:block;height:27px;border-bottom:1px solid var(--line)}

  .pen{position:absolute;left:70px;top:3200px;width:16px;height:440px;border-radius:8px;background:linear-gradient(90deg,#141b3a,#2d3a70,#141b3a)}
</style>
</head>
<body>

<!-- Business card front -->
<section class="piece card card-front white">
  <div class="brand dark"><span class="mark"></span>MuroDeck<br>Nordhaven</div>
  <div class="divider"></div>
  <div class="contact">
    <div class="person"><span class="first">HANNA</span> <span class="last">LINDQVIST</span></div>
    <div class="role">Co-Founder</div>
    <div>48 Fjordvik Road, Unit 12,<br>Nordhaven, NH 4021</div>
    <div><svg class="ico" viewBox="0 0 12 12"><path d="M3 1l2 3-1 1c1 2 2 3 3 3l1-1 3 2-1 2C5 11 1 7 1 2z" fill="#0b9bd8"/></svg>011 482 7730</div>
    <div><svg class="ico" viewBox="0 0 12 12"><rect x="1" y="2.5" width="10" height="7" fill="#0b9bd8"/><path d="M1 2.5l5 4 5-4" stroke="#fff" fill="none"/></svg>info@murodeck.example</div>
    <div><svg class="ico" viewBox="0 0 12 12"><circle cx="6" cy="6" r="5" fill="#0b9bd8"/></svg>www.murodeck.example</div>
  </div>
  <svg class="wave" viewBox="0 0 500 120" height="120" preserveAspectRatio="none">
    <path d="M0 120 V100 C140 110 220 40 500 20 V120 Z" fill="var(--blue)"/>
    <path d="M0 100 C140 110 220 40 500 20" fill="none" stroke="var(--orange)" stroke-width="3"/>
  </svg>
</section>

<!-- Business card back -->
<section class="piece card card-back blue">
  <div class="brand light"><span class="mark"></span>MuroDeck Nordhaven</div>
</section>

<!-- Letterhead -->
<section class="piece letterhead white">
  <header class="lh-head">
    <div class="brand dark"><span class="mark"></span>MuroDeck Nordhaven</div>
    <div class="addr">48 Fjordvik Road, Unit 12<br>Nordhaven, NH 4021<br>011 482 7730<br>info@murodeck.example</div>
  </header>
  <div class="lh-rule"></div>
  <article class="letter">
    <p>January 03, 2020</p>
    <p>Mr. Alex Rowan<br>President<br>Lumen Works<br>14 Harbor Lane, Suite 3<br>Eastvale, ER 40218</p>
    <p>Dear Mr. Rowan,</p>
    <p>We are pleased to share the latest wall printing options for your new office space. Our team has reviewed the measurements and prepared a proposal with three surface finishes and colour samples for each room.</p>
    <p>Each print is applied directly on the wall with durable inks that resist fading and can be cleaned easily. Installation takes one day per room and does not require moving furniture.</p>
    <p>Please let us know a suitable time for a short visit so we can confirm details and start scheduling.</p>
    <p>Regards,</p>
    <div class="sign">Erik Holm</div>
  </article>
  <svg class="wave" viewBox="0 0 600 170" height="170" preserveAspectRatio="none">
    <path d="M0 170 V20 C140 10 240 90 370 130 C470 160 540 150 600 140 V170 Z" fill="var(--blue)"/>
    <path d="M0 20 C140 10 240 90 370 130 C470 160 540 150 600 140" fill="none" stroke="var(--orange)" stroke-width="3"/>
  </svg>
</section>

<!-- Envelope front -->
<section class="piece env env-front white">
  <div class="brand dark"><span class="mark"></span>MuroDeck Nordhaven</div>
  <div class="addr">48 Fjordvik Road, Unit 12<br>Nordhaven, NH 4021</div>
  <svg class="wave" viewBox="0 0 520 150" height="150" preserveAspectRatio="none">
    <path d="M0 150 V0 C120 10 200 90 320 120 C400 140 470 140 520 138 V150 Z" fill="var(--blue)"/>
    <path d="M0 0 C120 10 200 90 320 120 C400 140 470 140 520 138" fill="none" stroke="var(--yellow)" stroke-width="3"/>
  </svg>
</section>

<!-- Envelope back -->
<section class="piece env env-back blue">
  <div class="brand light"><span class="mark"></span>MuroDeck Nordhaven</div>
</section>

<!-- Folder outside -->
<section class="folder folder-out">
  <div class="panel fold-back blue">
    <div class="brand light"><span class="mark"></span>MuroDeck Nordhaven</div>
    <div class="foot"><span>48 Fjordvik Road, Unit 12, Nordhaven, NH 4021</span><span>011 482 7730</span><span>info@murodeck.example</span><span>www.murodeck.example</span></div>
  </div>
  <div class="panel fold-front white">
    <div class="brand dark"><span class="mark"></span>MuroDeck Nordhaven</div>
    <svg class="wave" viewBox="0 0 420 120" height="120" preserveAspectRatio="none">
      <path d="M0 120 V70 C120 90 260 100 420 10 V120 Z" fill="var(--blue)"/>
      <path d="M0 70 C120 90 260 100 420 10" fill="none" stroke="var(--orange)" stroke-width="3"/>
    </svg>
  </div>
</section>

<!-- Folder inside -->
<section class="folder folder-in">
  <div class="panel white"><div class="pocket left"></div></div>
  <div class="panel white">
    <div class="insert">
      <div class="brand dark"><span class="mark"></span>MuroDeck Nordhaven</div>
      <div class="rule"></div>
      <p>January 03, 2020</p>
      <p>Dear Mr. Rowan,</p>
      <p>Thank you for choosing our studio. Enclosed you will find the print samples, the colour guide and the timeline for your project.</p>
    </div>
    <div class="pocket right"></div>
  </div>
</section>

<!-- Pen -->
<div class="pen" role="img" aria-label="Dark blue ballpoint pen"></div>

<!-- Cover -->
<section class="piece cover blue">
  <div class="brand light"><span class="mark"></span>MuroDeck Nordhaven</div>
</section>

<!-- Notepad -->
<section class="piece notepad white">
  <div class="brand dark"><span class="mark"></span>MuroDeck Nordhaven</div>
  <div class="date">Date: ..............</div>
  <div class="lines"><span></span><span></span><span></span><span></span><span></span><span></span><span></span><span></span><span></span><span></span><span></span><span></span><span></span><span></span><span></span><span></span></div>
  <svg class="wave" viewBox="0 0 420 40" height="40" preserveAspectRatio="none">
    <path d="M0 40 V22 C140 10 280 30 420 8 V40 Z" fill="var(--blue)"/>
    <path d="M0 22 C140 10 280 30 420 8" fill="none" stroke="var(--orange)" stroke-width="2"/>
  </svg>
</section>

</body>
</html>
```